July 4th Postcard to existing clients

5x7 postcard wishing our clients happy 4th of July. Card should read on the back "Thank You For Being A Valued Client!. Stay Safe And Enjoy Your Independence Day Celebrations!"

Patriotic theme with fireworks is ideal. We are a law firm so should still have a feel of professionalism while still being fun since it is for a fun holiday.

```html
<!DOCTYPE html>
<html lang="en">
<head>
<meta charset="utf-8">
<title>Hartwell Law – Independence Day Postcard</title>
<link rel="stylesheet" href="https://fonts.googleapis.com/css2?family=PT+Sans:wght@400;700&family=Lato:wght@300;400&display=swap">
<style>
  :root {
    --page: #ecebe8;
    --navy: #1c2d6b;
    --navy-deep: #14204f;
    --royal: #2a3f96;
    --banner-blue: #25348a;
    --sky: #7cb9f2;
    --red: #e42b36;
    --white: #ffffff;
    --ink: #4a5160;
    --mark: #b9c1e2;
    --flag-red: #b8323c;
    --flag-white: #ebe6e4;
    --canton: #3a4f9a;
  }
  * { margin: 0; padding: 0; box-sizing: border-box; }
  html, body { width: 1200px; height: 465px; overflow: hidden; }
  body { background: var(--page); position: relative; font-family: "PT Sans", sans-serif; }

  .postcard { position: absolute; top: 36px; height: 388px; overflow: hidden; box-shadow: 0 2px 6px rgba(0,0,0,.18); }
  .postcard--front { left: 40px; width: 543px; background: var(--navy); }
  .postcard--back { left: 625px; width: 535px; background: var(--white); }

  /* Front: flag photo area in its main tones, stripes as plain bands */
  .front-photo {
    position: absolute; left: 0; top: 0; width: 543px; height: 272px;
    background:
      linear-gradient(180deg, transparent 0 78%, rgba(233,200,205,.75) 100%),
      linear-gradient(90deg, var(--canton) 0 246px, transparent 246px) top left / 100% 162px no-repeat,
      repeating-linear-gradient(180deg, var(--flag-red) 0 20px, var(--flag-white) 20px 40px);
  }
  .front-photo::after {
    content: ""; position: absolute; inset: 0;
    background: radial-gradient(ellipse at 75% 45%, rgba(120,150,150,.35) 0%, transparent 60%),
                radial-gradient(ellipse at 25% 75%, rgba(90,70,60,.3) 0%, transparent 55%);
  }
  .greeting-band {
    position: absolute; left: 0; top: 212px; width: 543px; height: 54px;
    background: rgba(255,255,255,.38);
  }
  .greeting-rule { position: absolute; left: 52px; width: 438px; height: 2px; background: var(--banner-blue); }
  .greeting-rule--top { top: 218px; }
  .greeting-rule--bottom { top: 260px; }
  .greeting {
    position: absolute; left: 52px; top: 220px; width: 438px; height: 40px;
    display: flex; align-items: center; justify-content: center; gap: 14px;
    color: var(--banner-blue); font-weight: 400; font-size: 35px; letter-spacing: .5px; line-height: 1;
  }
  .greeting .star { font-size: 17px; }

  .front-brand {
    position: absolute; left: 0; top: 272px; width: 543px; height: 116px;
    background: linear-gradient(180deg, var(--navy) 0%, var(--navy-deep) 100%);
    display: flex; flex-direction: column; align-items: center; justify-content: center; gap: 12px;
  }
  .brand-square { width: 34px; height: 34px; background: var(--mark); }
  .brand-name { font-family: "Lato", sans-serif; font-weight: 300; font-size: 25px; letter-spacing: 1.5px; color: var(--mark); }

  /* Back: confetti area in its main tones */
  .back-art {
    position: absolute; left: 0; top: 0; width: 270px; height: 388px;
    background:
      radial-gradient(ellipse at 20% 15%, rgba(124,185,242,.35) 0%, transparent 30%),
      radial-gradient(ellipse at 80% 20%, rgba(228,43,54,.3) 0%, transparent 28%),
      radial-gradient(ellipse at 25% 85%, rgba(228,43,54,.3) 0%, transparent 28%),
      radial-gradient(ellipse at 75% 88%, rgba(124,185,242,.3) 0%, transparent 30%),
      radial-gradient(ellipse at 50% 45%, var(--royal) 0%, var(--navy) 55%, var(--navy-deep) 100%);
  }
  .message {
    position: absolute; left: 35px; top: 108px; width: 200px; height: 153px;
    border: 2px solid var(--white);
    display: flex; flex-direction: column; align-items: center; justify-content: center;
    text-align: center; text-transform: uppercase; line-height: 1.05;
  }
  .message__thanks { color: var(--sky); font-size: 15px; }
  .message__ribbon {
    margin: 3px 0; padding: 1px 16px; background: var(--red); color: var(--white); font-size: 15px;
    clip-path: polygon(0 0, 100% 0, 94% 50%, 100% 100%, 0 100%, 6% 50%);
  }
  .message__safe { color: var(--white); font-weight: 700; font-size: 27px; }
  .message__enjoy { color: var(--sky); font-size: 14px; }
  .message__holiday { color: var(--red); font-weight: 700; font-size: 17px; }

  .mailing { position: absolute; left: 270px; top: 0; width: 265px; height: 388px; }
  .mailing__brand { position: absolute; left: 0; top: 20px; width: 216px; display: flex; flex-direction: column; align-items: center; gap: 8px; }
  .mailing__square { width: 26px; height: 26px; background: var(--mark); }
  .mailing__name { font-family: "Lato", sans-serif; font-weight: 400; font-size: 18px; letter-spacing: 1.5px; color: var(--ink); }
  .mailing__address { position: absolute; left: 63px; top: 84px; font-size: 12px; line-height: 1.4; color: #222; font-style: normal; }
  .stamp { position: absolute; left: 192px; top: 19px; width: 53px; height: 63px; border: 2px dashed #9a9a9a; }
</style>
</head>
<body>
  <section class="postcard postcard--front">
    <div class="front-photo" role="img" aria-label="Photo of a waving American flag with stars, the Statue of Liberty and marching soldiers"></div>
    <div class="greeting-band"></div>
    <div class="greeting-rule greeting-rule--top"></div>
    <div class="greeting-rule greeting-rule--bottom"></div>
    <h1 class="greeting"><span class="star">★</span><span>HAPPY&nbsp;&nbsp;4TH OF JULY</span><span class="star">★</span></h1>
    <div class="front-brand">
      <div class="brand-square"></div>
      <div class="brand-name">HARTWELL LAW</div>
    </div>
  </section>

  <section class="postcard postcard--back">
    <div class="back-art" role="img" aria-label="Red and light blue confetti falling on a deep blue background"></div>
    <div class="message">
      <p class="message__thanks">Thank you for being</p>
      <p class="message__ribbon">A valued client</p>
      <p class="message__safe">Stay safe</p>
      <p class="message__enjoy">and enjoy your</p>
      <p class="message__holiday">Independence Day<br>Celebrations!</p>
    </div>
    <div class="mailing">
      <div class="mailing__brand">
        <div class="mailing__square"></div>
        <div class="mailing__name">HARTWELL LAW</div>
      </div>
      <address class="mailing__address">1470 W Maple Crest Ave<br>Fairview, MO 65810</address>
      <div class="stamp"></div>
    </div>
  </section>
</body>
</html>
```